Hip Surgeon needs a web page re-design.

I have a web page to provide information about the diseases of the hip joint for the patients from my private practice since 2008. I need a re-design job for a fresh new look.
We have made a new logo and a new stationery design here in CraftLoomery (please see the uploaded files) and I want to make my web page look-alike the new design concepts.
I like the color blue and tones of blue, matching my logo and stationery.
I don't like "busy" designs. It must be clean, elegant and ease to read. The final design should be "mobile friendly" if possible.
Please visit my website www.pontevivaclinica.com.br to take a look and get some inspiration.

```html
<!DOCTYPE html>
<html lang="en">
<head>
<meta charset="utf-8">
<title>Dr. Marcos Lacerda Andrade – Cirurgia do Quadril</title>
<link href="https://fonts.googleapis.com/css2?family=Open+Sans:wght@400;600;700&family=Raleway:wght@400;600;800;900&display=swap" rel="stylesheet">
<style>
:root{
  --blue:#1f6dc2;
  --blue-dark:#17569c;
  --blue-band:#2a76cf;
  --ink:#1d1d1d;
  --dark:#1b1b1b;
  --footer:#222325;
  --footer-bottom:#161718;
  --grey:#8a8a8a;
  --light:#f2f2f2;
  --green:#6aa329;
  --orange:#e8542a;
  --yellow:#e9b423;
  --white:#ffffff;
}
*{box-sizing:border-box;margin:0;padding:0}
html,body{width:1200px;height:2874px;overflow:hidden}
body{font-family:"Open Sans",Arial,sans-serif;color:var(--ink);background:var(--white);position:relative}
.abs{position:absolute}

/* hero */
.hero{position:absolute;left:0;top:0;width:1200px;height:660px;background:linear-gradient(135deg,#d9e6ee 0%,#7fb3c7 35%,#2f8fa8 60%,#1f5f7a 100%)}
.top-btn{position:absolute;top:29px;height:44px;border-radius:4px;color:#fff;font-size:12px;line-height:14px;padding:8px 12px 0 42px;font-weight:700}
.top-btn small{display:block;font-weight:400;font-size:11px}
.top-btn svg{position:absolute;left:14px;top:13px}
.btn-login{left:742px;width:168px;background:var(--blue)}
.btn-register{left:927px;width:175px;background:#111}
.slide-arrow{position:absolute;top:335px;width:36px;height:38px;display:flex;align-items:center;justify-content:center}
.arrow-left{left:53px;background:#111}
.arrow-right{left:1109px;background:var(--yellow)}
.logo-box{position:absolute;left:120px;top:510px;width:306px;height:120px;background:#fff;border:3px solid #cfd9e4;display:flex;align-items:center;padding-left:16px;gap:14px}
.logo-box .mark{width:54px;height:54px;border-radius:50%;border:4px solid var(--blue)}
.logo-name{font-family:"Raleway",sans-serif;font-weight:600;color:var(--blue);font-size:24px;line-height:28px}
.logo-name small{display:block;font-size:16px;font-weight:600}
.caption{position:absolute;left:431px;top:510px;width:647px;height:120px;background:rgba(31,109,194,.92);color:#fff;text-align:center;padding-top:30px;font-family:Georgia,serif}
.caption h2{font-size:19px;font-weight:700;letter-spacing:.5px}
.caption p{font-size:13px;font-style:italic;margin-top:8px}
.dots{position:absolute;left:1015px;top:606px;display:flex;gap:4px}
.dots i{width:10px;height:10px;background:#2b3a4a}
.dots i.on{background:#cfd9e4}

/* nav */
.nav{position:absolute;left:0;top:660px;width:1200px;height:46px;background:#1a1a1a}
.nav ul{list-style:none;display:flex;position:absolute;left:137px;top:0}
.nav li{height:46px;line-height:46px;color:#fff;font-size:12px;font-weight:600;text-align:center;border-right:1px solid #333;padding:0 25px}
.nav li.active{background:var(--blue)}

/* features */
.feature{position:absolute;top:760px;width:300px}
.feature .icon{width:90px;height:90px;border-radius:50%;background:#6c6c6c;margin-left:105px;display:flex;align-items:center;justify-content:center}
.feature.active .icon{background:var(--blue)}
.feature h3{margin-top:44px;font-size:16px;font-weight:700;display:flex;align-items:center;gap:8px}
.feature.active h3{color:var(--blue)}
.feature p{margin-top:10px;font-size:12px;line-height:17px;color:var(--grey)}
.feature .more{margin-top:18px;text-align:right;font-size:13px;color:#333}
.feature.active .more{color:var(--blue)}

/* welcome */
.welcome{position:absolute;left:0;top:1035px;width:1200px;height:83px;background:var(--blue-band)}
.welcome h2{position:absolute;left:93px;top:25px;font-family:"Raleway",sans-serif;font-weight:400;color:#fff;font-size:28px}
.welcome .brochure{position:absolute;left:860px;top:20px;width:242px;height:43px;border:2px solid #fff;color:#fff;font-size:17px;font-style:italic;text-align:center;line-height:39px}

/* about */
.about{position:absolute;left:0;top:1118px;width:1200px;height:350px;background:var(--dark);text-align:center}
.about h2{margin-top:42px;font-family:"Raleway",sans-serif;font-weight:900;color:#fff;font-size:46px}
.about .sub{font-family:"Raleway",sans-serif;color:var(--blue);font-size:22px;margin-top:2px}
.about p{color:#8d8d8d;font-size:15px;line-height:26px;margin:22px auto 0;width:1110px}
.about p + p{margin-top:12px}
.btn-learn{position:absolute;left:517px;top:282px;width:166px;height:40px;background:var(--green);border:2px solid #fff;color:#fff;font-size:17px;font-style:italic;line-height:36px}

/* gallery */
.section-title{position:absolute;left:0;width:1200px;text-align:center;font-family:"Raleway",sans-serif;font-weight:900;font-size:50px;color:var(--ink)}
.section-sub{position:absolute;left:0;width:1200px;text-align:center;font-family:"Raleway",sans-serif;font-size:18px;color:var(--blue)}
.rule{position:absolute;top:1592px;height:1px;width:110px;background:#ddd}
.filters{position:absolute;left:0;top:1645px;width:1200px;display:flex;justify-content:center;gap:6px}
.filters span{height:25px;line-height:25px;padding:0 10px;background:#3a3a3a;color:#fff;font-size:12px}
.filters span.on{background:var(--blue)}
.card{position:absolute;top:1703px;width:321px;height:256px;border:1px solid #e2e2e2;background:#fff}
.card .photo{height:189px;position:relative}
.card .tag{position:absolute;left:0;bottom:0;height:40px;line-height:40px;padding:0 16px;background:var(--blue);color:#fff;font-size:15px;font-weight:700}
.card p{padding:10px 14px;font-size:13px;line-height:17px;color:#666}

/* partners */
.partners{position:absolute;left:0;top:1983px;width:1200px;height:352px;background:linear-gradient(180deg,var(--blue) 0%,#2b7fd6 100%)}
.partners .section-title{color:#fff;font-size:44px}
.partners .section-sub{color:#fff;font-size:24px;font-weight:600}
.badge{position:absolute;top:2130px;width:156px;height:156px;border-radius:50%;background:#fff;border:8px solid #1a5fae;display:flex;align-items:center;justify-content:center}
.badge i{width:86px;height:86px;border-radius:50%;background:#dfe6ee}

/* promos */
.promo{position:absolute;top:2359px;height:77px;border:1px solid #d9d9d9;background:#fff;display:flex;align-items:center;overflow:hidden}
.promo .pic{height:100%;width:42%}
.promo .txt{padding-left:12px;font-size:11px;line-height:14px;color:#555;text-transform:uppercase}
.promo .txt b{color:var(--blue);display:block}

/* newsletter */
.newsletter{position:absolute;left:0;top:2455px;width:1200px;height:88px;background:var(--blue)}
.newsletter .label{position:absolute;left:162px;top:24px;color:#fff;font-size:16px;font-weight:600;line-height:20px}
.field{position:absolute;top:24px;width:282px;height:43px;background:#fff;font-size:13px;color:#999;line-height:43px;padding-left:20px}
.subscribe{position:absolute;left:960px;top:24px;width:140px;height:43px;background:var(--orange);color:#fff;font-weight:700;font-size:14px;text-align:center;line-height:43px}

/* footer */
.footer{position:absolute;left:0;top:2543px;width:1200px;height:283px;background:var(--footer);color:#cfcfcf;font-size:12px;line-height:18px}
.footer h4{color:#fff;font-size:14px;font-weight:700;margin-bottom:18px}
.fcol{position:absolute;top:33px}
.contact-row{display:flex;gap:14px;margin-bottom:10px}
.contact-row svg{flex:none;margin-top:3px}
.social{display:flex;gap:14px;margin-bottom:14px}
.social i{width:16px;height:16px;border-radius:50%;background:#8a8a8a}
.social i.on{background:var(--blue)}
.f-email{width:286px;height:36px;background:#fff;color:#999;font-size:11px;line-height:36px;padding-left:12px;position:relative;margin-top:10px}
.to-top{position:absolute;left:1090px;top:30px;width:44px;height:44px;border-radius:50%;border:2px solid #444}
.bottom-bar{position:absolute;left:0;top:2826px;width:1200px;height:48px;background:var(--footer-bottom);color:#bbb;font-size:12px;line-height:48px}
.bottom-bar .copy{position:absolute;left:96px}
.bottom-bar .links{position:absolute;right:96px;display:flex;gap:28px}
</style>
</head>
<body>

<section class="hero" role="img" aria-label="Surgical team in blue scrubs operating under theatre lights">
  <a class="top-btn btn-login"><svg width="14" height="16" viewBox="0 0 14 16"><rect x="1" y="7" width="12" height="9" rx="1" fill="#fff"/><path d="M4 7V5a3 3 0 016 0v2" stroke="#fff" stroke-width="2" fill="none"/></svg>CLIENT LOGIN<small>Create new account</small></a>
  <a class="top-btn btn-register"><svg width="14" height="16" viewBox="0 0 14 16"><rect x="1" y="7" width="12" height="9" rx="1" fill="#fff"/><path d="M4 7V5a3 3 0 016 0v2" stroke="#fff" stroke-width="2" fill="none"/></svg>REGISTER NOW<small>Access your dashboard</small></a>
  <span class="slide-arrow arrow-left"><svg width="10" height="12"><path d="M8 1L2 6l6 5" stroke="#fff" stroke-width="2" fill="none"/></svg></span>
  <span class="slide-arrow arrow-right"><svg width="10" height="12"><path d="M2 1l6 5-6 5" stroke="#222" stroke-width="2" fill="none"/></svg></span>
  <div class="logo-box"><span class="mark"></span><div class="logo-name">Dr. Marcos L. Andrade<small>Cirurgia Do Quadril</small></div></div>
  <div class="caption"><h2>LOREM IPSUM IS SIMPLY A DUMMY TEXT</h2><p>Contrary to popular belief, Lorem Ipsum is not simply random text. It has roots in a piece of classical Latin</p></div>
  <div class="dots"><i></i><i class="on"></i><i></i><i></i></div>
</section>

<nav class="nav"><ul>
  <li class="active">HOME</li><li>ABOUT</li><li>SAIBA MAIS</li><li>CURRICULUM VITAE</li><li>LINKS</li><li>DOWNLOADS</li><li>ATUALIDADES</li><li>CONTATO</li>
</ul></nav>

<div class="feature" style="left:95px">
  <div class="icon"><svg width="40" height="40" viewBox="0 0 40 40"><path d="M20 4v32M12 12c8-4 16 4 8 8s0 12 8 8" stroke="#fff" stroke-width="3" fill="none"/></svg></div>
  <h3><svg width="14" height="14"><circle cx="7" cy="7" r="6" fill="#1d1d1d"/></svg>LOREM IPSUM IS SIMPLY DUMMY</h3>
  <p>Sed ut perspiciatis unde omnis iste natus error sit voluptatem accusantium doloremque laudan, totam rem aperiam, eaque ipsa quae ab.</p>
  <div class="more">➜ &nbsp;Show me more</div>
</div>
<div class="feature" style="left:455px">
  <div class="icon"><svg width="40" height="40" viewBox="0 0 40 40"><rect x="6" y="12" width="28" height="22" rx="3" fill="#fff"/><path d="M15 12V8h10v4" stroke="#fff" stroke-width="3" fill="none"/><path d="M20 17v12M14 23h12" stroke="#6c6c6c" stroke-width="4"/></svg></div>
  <h3><svg width="14" height="14"><rect x="1" y="2" width="12" height="11" rx="2" fill="#1d1d1d"/></svg>LOREM IPSUM IS SIMPLY DUMMY</h3>
  <p>Sed ut perspiciatis unde omnis iste natus error sit voluptatem accusantium doloremque laudan, totam rem aperiam, eaque ipsa quae ab.</p>
  <div class="more">➜ &nbsp;Show me more</div>
</div>
<div class="feature active" style="left:820px">
  <div class="icon"><svg width="40" height="40" viewBox="0 0 40 40"><path d="M10 30l16-16M22 10l8 8M28 8l4 4M10 30l-4 4" stroke="#fff" stroke-width="4" fill="none"/></svg></div>
  <h3><svg width="14" height="14"><path d="M2 12l8-8M9 2l3 3" stroke="#1f6dc2" stroke-width="2"/></svg>LOREM IPSUM IS SIMPLY DUMMY</h3>
  <p>Sed ut perspiciatis unde omnis iste natus error sit voluptatem accusantium doloremque laudan, totam rem aperiam, eaque ipsa quae ab.</p>
  <div class="more">➜ &nbsp;Show me more</div>
</div>

<section class="welcome"><h2>Welcome to DR. MARCOS LACERDA ANDRADE</h2><span class="brochure">DOWNLOAD BROCHURE</span></section>

<section class="about">
  <h2>ABOUT US</h2>
  <div class="sub">DR. MARCOS LACERDA ANDRADE</div>
  <p>Seja bem vindo ao site "Ponte Viva"!</p>
  <p>O objetivo deste site é fornecer ao público leigo informações sobre as principais doenças e procedimentos cirúrgicos envolvendo o quadril e a pelve, como próteses de quadril, artroscopia (cirurgia por vídeo), etc.</p>
  <span class="btn-learn">LEARN MORE</span>
</section>

<h2 class="section-title" style="top:1496px">PICTURE GALLERY</h2>
<span class="rule" style="left:392px"></span><span class="rule" style="left:698px"></span>
<div class="section-sub" style="top:1570px">DR. MARCOS LACERDA ANDRADE</div>
<svg class="abs" style="left:560px;top:1610px" width="80" height="16"><g fill="#bbb"><rect x="0" y="2" width="12" height="12"/><rect x="34" y="2" width="12" height="12" fill="#555"/><rect x="68" y="2" width="12" height="12"/></g></svg>
<div class="filters"><span class="on">All</span><span>Clinic</span><span>Diagrams</span><span>XRays</span></div>

<article class="card" style="left:96px"><div class="photo" role="img" aria-label="Anatomical diagram of the hip joint" style="background:linear-gradient(135deg,#c9b8a6,#8a7564)"><span class="tag">DIAGRAMS</span></div><p>Contrary to popular belief, Lorem Ipsum is not simply random text.</p></article>
<article class="card" style="left:438px"><div class="photo" role="img" aria-label="Hospital corridor with medical staff" style="background:linear-gradient(135deg,#bfe3ea,#3c8fa8)"><span class="tag">CLICNIC</span></div><p>Contrary to popular belief, Lorem Ipsum is not simply random text.</p></article>
<article class="card" style="left:778px"><div class="photo" role="img" aria-label="Pelvis X-ray image" style="background:radial-gradient(circle at 50% 45%,#9a9a9a,#2a2a2a)"><span class="tag">XRAYS</span></div><p>Contrary to popular belief, Lorem Ipsum is not simply random text.</p></article>

<section class="partners">
  <h2 class="section-title" style="top:36px">OUR PARTNERS</h2>
  <div class="section-sub" style="top:86px">DR. MARCOS LACERDA ANDRADE</div>
</section>
<div class="badge" style="left:300px"><i></i></div>
<div class="badge" style="left:521px"><i></i></div>
<div class="badge" style="left:741px"><i></i></div>

<div class="promo" style="left:96px;width:251px"><div class="pic" role="img" aria-label="Hip prosthesis model" style="background:linear-gradient(135deg,#e6e6e6,#b5b5b5)"></div><div class="txt"><b>Saiba mais</b>Próteses de quadril</div></div>
<div class="promo" style="left:359px;width:228px"><div class="txt" style="width:55%"><b>Agende sua</b>consulta</div><div class="pic" role="img" aria-label="Receptionist with headset" style="background:linear-gradient(135deg,#f0d6c2,#b98a6a)"></div></div>
<div class="promo" style="left:606px;width:237px"><div class="pic" style="background:#d8302a;width:45%"></div><div class="txt"><b>Canal Ponte Viva</b>Veja nosso canal</div></div>
<div class="promo" style="left:862px;width:240px"><div class="txt" style="width:55%"><b>Saiba mais</b>Artroscopia do quadril</div><div class="pic" role="img" aria-label="Arthroscopy instrument illustration" style="background:linear-gradient(135deg,#e8e8e8,#b0b0b0)"></div></div>

<section class="newsletter">
  <svg class="abs" style="left:93px;top:26px" width="44" height="38" viewBox="0 0 44 38"><path d="M2 18L42 2 34 36 20 24 2 18zM20 24l22-22" stroke="#fff" stroke-width="2.5" fill="none" stroke-linejoin="round"/></svg>
  <div class="label">Subscribe to<br>our Newsletter</div>
  <div class="field" style="left:349px">Enter Your Name</div>
  <div class="field" style="left:656px">Enter Your Email Address</div>
  <div class="subscribe">SUBSCRIBE</div>
</section>

<footer class="footer">
  <div class="fcol" style="left:96px;width:300px">
    <h4>ABOUT US</h4>
    <p>Lorem ipsum dolor sit amet elit, consectetur adipiscing. Vestibulum luctus ipsum id quam euismod a malesuada sapien euismot.</p>
    <p style="margin-top:18px">Clínica Ponte Viva,<br>Rua das Acácias 120, Curitiba<br>Brasil, 80010-000</p>
  </div>
  <div class="fcol" style="left:455px;width:300px">
    <h4>CONTACT INFORMATION</h4>
    <div class="contact-row"><svg width="14" height="12"><path d="M7 0L0 6h2v6h10V6h2z" fill="#ccc"/></svg><span>Company Name<br>Address 1<br>Address 2<br>Town<br>Zip Code</span></div>
    <div class="contact-row"><svg width="14" height="14"><path d="M3 1l3 3-2 2c1 2 2 3 4 4l2-2 3 3-2 2C6 13 1 8 1 3z" fill="#ccc"/></svg><span>01234 567890</span></div>
    <div class="contact-row"><svg width="14" height="11"><rect x="0" y="0" width="14" height="11" fill="#ccc"/><path d="M0 0l7 6 7-6" stroke="#222" fill="none"/></svg><span style="color:#5a9be0">contato@pontevivaclinica.com.br</span></div>
  </div>
  <div class="fcol" style="left:816px;width:300px">
    <h4>CONNECT WITH US</h4>
    <div class="social"><i></i><i class="on"></i><i></i><i></i><i></i><i></i></div>
    <div style="border-top:1px solid #3a3a3a;padding-top:12px;font-size:11px">Sign up to our newsletter:</div>
    <div class="f-email">ENTER YOUR EMAIL ADDRESS HERE<svg class="abs" style="right:10px;top:13px" width="14" height="11"><rect width="14" height="11" fill="#888"/><path d="M0 0l7 6 7-6" stroke="#fff" fill="none"/></svg></div>
  </div>
  <span class="to-top"><svg class="abs" style="left:13px;top:14px" width="14" height="10"><path d="M1 8l6-6 6 6" stroke="#777" stroke-width="2" fill="none"/></svg></span>
</footer>

<div class="bottom-bar"><span class="copy">@ Copyright 2014 Dr. Marcos Lacerda Andrade</span><span class="links"><span>Home</span><span>Our Blog</span><span>Contact Us</span></span></div>

</body>
</html>
```